Harbo Hale - A non profit for healthy lifestyle and fitness within refugee camps

We need a logo and website design for a new 501c3 Non-Profit based in San Francisco called 'Harbo Hale'. We help coordinate trips across the globe to provide fitness classes to refugee camps to help refugees maintain a healthy lifestyle and fun while exercising.
Our first trip was to Greece and we hope to extend our reach by working with other non-profits to coordinate how we can help bring a healthy lifestyle and a wellness to refugees in need.
We would like to see website design that use the color green and blue. The final design should represent a welcoming website to encourage people to take a trip either by themselves, as a group, or with a corporate team.
We have 3 certified and experienced trainers that will be running these trips and with a hope of 20 volunteers per trip to help.

We are hoping to partner with another 501c3 called 'Tide to Dawn' which I have participated in and with the hopes of providing an easier and simpler user experience than their current website but with many of the same content.

We would like a 'Trips' page with previous trips, 'Trainers/Hosts' page with bios of the leaders hosting the event, 'Register Page' for folks to register for upcoming trips, 'About Us' page for our mission statement and work, 'Albums' page for photos taken on the trip, 'Contact Us' page for FAQs and questions to submit, and a 'Donate' page for people to donate to our cause.

I would like this page to be created in Word Press.

ie: http://www.tidetodawn-example.com.au/programs/

Target Market(s)

Volunteers, non-profit partners

Industry/Entity Type

Non-Profit

Number of Pages Required

4 page

Font styles to use
Sans Serif

Colors

Designer to choose colors to be used in the design.

Requirements
Must have
• 'Trips' page with previous trips, 'Trainers/Hosts' page with bios of the leaders hosting the event, 'Register Page' for folks to register for upcoming trips, 'About Us' page for our mission statement and work, 'Albums' page for photos taken on the trip, 'Contact Us' page for FAQs and questions to submit, and a 'Donate' page for people to donate to our cause.

```html
<!DOCTYPE html>
<html lang="en">
<head>
<meta charset="utf-8">
<title>Harbo Hale — Fitness for Refugee Camps</title>
<link href="https://fonts.googleapis.com/css2?family=Open+Sans:wght@400;600;700&family=Roboto+Slab:wght@400;700&display=swap" rel="stylesheet">
<style>
:root{
  --green:#8cc63f;
  --green-dark:#76ad2f;
  --blue:#19aee0;
  --blue-deep:#0f93c4;
  --ink:#2e343c;
  --ink-deep:#24292f;
  --text:#6b7178;
  --muted:#9aa0a6;
  --white:#ffffff;
  --paper:#ffffff;
}
*{box-sizing:border-box;margin:0;padding:0}
html,body{width:1200px;height:3168px;overflow:hidden;background:var(--paper)}
body{font-family:"Open Sans",Arial,sans-serif;color:var(--text);font-size:13px;line-height:1.6}
.page{position:relative;width:1200px;height:3168px;overflow:hidden}
.btn{display:inline-block;background:var(--green);color:var(--white);font-size:11px;font-weight:700;letter-spacing:1px;text-transform:uppercase;padding:8px 22px;line-height:1.4}

/* Header + hero */
.hero{position:absolute;left:0;top:0;width:1200px;height:620px}
.hero-photo{position:absolute;inset:0;background:linear-gradient(180deg,#c9dde6 0%,#e6eef0 35%,#d8cbb9 70%,#b79f84 100%)}
.site-nav{position:absolute;left:0;top:0;width:1200px;height:52px;background:rgba(25,174,224,.6);display:flex;align-items:center;padding:0 40px}
.brand{display:flex;align-items:center;gap:10px;font-family:"Roboto Slab",Georgia,serif;font-weight:700;font-size:24px;color:var(--white)}
.brand-dot{width:14px;height:14px;border-radius:50%;background:var(--green)}
.nav-links{margin-left:auto;display:flex;align-items:center;gap:26px;list-style:none}
.nav-links li{font-size:11px;font-weight:600;color:var(--white);text-transform:uppercase;letter-spacing:.5px}
.nav-links li.active{background:var(--green);padding:4px 10px}
.hero-badge{position:absolute;left:855px;top:290px;width:240px;height:240px;border-radius:50%;background:var(--green);display:flex;flex-direction:column;align-items:center;justify-content:center;text-align:center;color:var(--white);padding:0 30px}
.hero-badge p{font-family:"Roboto Slab",Georgia,serif;font-size:16px;line-height:1.4}
.hero-badge strong{color:#3d5a12;text-transform:uppercase;font-weight:700}
.hero-badge .btn{background:var(--white);color:var(--green);margin-top:14px}

/* Intro band */
.intro{position:absolute;left:0;top:600px;width:1200px;height:260px;background:var(--ink);border-bottom:6px solid var(--green)}
.intro-cols{position:absolute;left:0;top:60px;width:1200px;display:flex;justify-content:center;gap:160px}
.intro-col{width:360px;text-align:center;color:#b8bec4}
.intro-col h3{font-family:"Roboto Slab",Georgia,serif;color:var(--green);font-size:15px;font-weight:400;text-transform:uppercase;margin-bottom:10px}
.intro-col p{font-size:12px;margin-bottom:22px}

/* Trainers */
.section-title{position:absolute;left:0;width:1200px;text-align:center;font-family:"Roboto Slab",Georgia,serif;font-weight:400;color:var(--green);font-size:15px;text-transform:uppercase;letter-spacing:1px}
.tabs{position:absolute;left:0;top:1050px;width:1200px;display:flex;justify-content:center;gap:10px}
.tab{width:82px;height:22px;border:1px solid #d5d8db;font-size:10px;text-align:center;line-height:20px;color:var(--muted)}
.tab.active{background:var(--green);border-color:var(--green);color:var(--white)}
.team-grid{position:absolute;left:0;top:1100px;width:1200px;display:grid;grid-template-columns:repeat(6,200px);grid-auto-rows:280px}
.member{position:relative}
.member-photo{position:absolute;left:0;top:0;width:200px;height:240px}
.member-name{position:absolute;left:0;top:240px;width:200px;height:40px;font-size:11px;text-align:center;line-height:40px;color:var(--text)}
.member.featured .member-name{background:var(--green);color:var(--white)}
.member.featured .member-more{position:absolute;left:0;top:200px;width:200px;height:40px;background:rgba(140,198,63,.9);color:var(--white);font-size:11px;text-align:center;line-height:40px}
.tone-a{background:linear-gradient(160deg,#e8ddd4,#b7a18f)}
.tone-b{background:linear-gradient(160deg,#d7d7d5,#8e8a86)}
.tone-c{background:linear-gradient(160deg,#e9e3dc,#c9b7a4)}
.tone-d{background:linear-gradient(160deg,#9c938c,#55504c)}
.tone-e{background:linear-gradient(160deg,#dfe2e4,#a6a9ac)}
.tone-f{background:linear-gradient(160deg,#efe9e4,#cdb6a3)}
.more-row{position:absolute;left:0;width:1200px;text-align:center}

/* About */
.about{position:absolute;left:0;top:1820px;width:1200px;height:420px;background:var(--blue)}
.about-text{position:absolute;left:40px;top:40px;width:680px;color:#e5f6fc}
.about-text h2{font-family:"Roboto Slab",Georgia,serif;font-weight:400;font-size:40px;line-height:1.2;color:var(--white);margin-bottom:16px}
.about-text p{font-size:11.5px;margin-bottom:12px}
.stats{display:flex;gap:50px;margin-top:24px}
.stat{display:flex;align-items:baseline;gap:8px;color:var(--white)}
.stat b{font-family:"Roboto Slab",Georgia,serif;font-size:26px;font-weight:400}
.stat span{font-size:10px;text-transform:uppercase}
.about-photo{position:absolute;left:760px;top:0;width:440px;height:420px;background:linear-gradient(150deg,#e4e6e3 0%,#c7d3d6 45%,#7bb83a 75%,#5b8f2b 100%)}

/* Camps */
.camps{position:absolute;left:0;top:2370px;width:1200px;display:grid;grid-template-columns:repeat(3,400px)}
.camp-photo{height:250px}
.camp-body{height:70px;text-align:center;padding-top:12px}
.camp-meta{font-size:10px;color:var(--muted);display:flex;justify-content:center;gap:18px}
.camp-title{font-size:10px;text-transform:uppercase;color:var(--text);margin-top:6px}
.camp.featured .camp-body{background:var(--green)}
.camp.featured .camp-meta,.camp.featured .camp-title{color:var(--white)}
.camp-1{background:linear-gradient(150deg,#f3efe4,#a7d17a 60%,#e06b9b)}
.camp-2{background:linear-gradient(180deg,#cfd6d4,#9fb4b6 55%,#d6c4a2)}
.camp-3{background:linear-gradient(150deg,#3ea8d8,#b9629c 55%,#5fb3d6)}

/* Partners */
.partners{position:absolute;left:0;top:2780px;width:1200px;height:140px;display:flex;justify-content:center;align-items:center;gap:46px}
.partner{height:100px;border-radius:8px}

/* Footer */
.footer{position:absolute;left:0;top:2960px;width:1200px;height:208px;background:var(--ink);border-top:6px solid var(--green)}
.footer-cols{position:absolute;left:150px;top:40px;width:900px;display:flex;gap:60px}
.footer-col h4{font-family:"Roboto Slab",Georgia,serif;font-weight:400;color:var(--green);font-size:12px;text-transform:uppercase;margin-bottom:8px}
.footer-col p{font-size:10px;color:#a9afb5;line-height:1.55}
.social{display:flex;gap:6px}
.social i{width:24px;height:24px;display:block}
.footer-bar{position:absolute;left:0;bottom:0;width:1200px;height:34px;background:var(--ink-deep);display:flex;align-items:center;padding:0 150px;font-size:10px;color:#8d949a}
.footer-bar ul{list-style:none;display:flex;gap:16px;margin:0 auto}
.footer-bar li.active{color:var(--green)}
</style>
</head>
<body>
<div class="page">

  <header class="hero">
    <div class="hero-photo" role="img" aria-label="Photo of two fitness trainers sitting on medicine balls in a bright gym"></div>
    <nav class="site-nav">
      <div class="brand"><span class="brand-dot"></span>Harbo Hale</div>
      <ul class="nav-links">
        <li>Home</li><li>About us</li><li>Trips</li><li>Trainers/Hosts</li><li>Registration</li><li>Albums</li><li class="active">Contact us</li><li>Donate</li>
      </ul>
    </nav>
    <div class="hero-badge">
      <p>Lorem ipsum sit <strong>dolor</strong> &amp; professional <strong>fitness class</strong> sed &amp; volunteers</p>
      <span class="btn">Donate now</span>
    </div>
  </header>

  <section class="intro">
    <div class="intro-cols">
      <div class="intro-col">
        <h3>Summer camps for children</h3>
        <p>Lorem ipsum dolor sit amet, consectetur adipiscing elit sed diam nonummy nibh euismod tincidunt ut laoreet dolore magna aliquam erat volutpat.</p>
        <span class="btn">Join us</span>
      </div>
      <div class="intro-col">
        <h3>Become our volunteer</h3>
        <p>Consectetur adipiscing elit sed diam nonummy nibh euismod tincidunt ut laoreet dolore magna aliquam erat volutpat.</p>
        <span class="btn">Join us</span>
      </div>
    </div>
  </section>

  <h2 class="section-title" style="top:1000px">Meet our trainers and volunteers</h2>
  <div class="tabs"><span class="tab">All</span><span class="tab active">Trainers</span><span class="tab">Volunteers</span></div>

  <div class="team-grid">
    <div class="member"><div class="member-photo tone-a" role="img" aria-label="Photo of a trainer exercising"></div><div class="member-name">Mara Lintz</div></div>
    <div class="member"><div class="member-photo tone-f" role="img" aria-label="Photo of a trainer with a ponytail"></div><div class="member-name">Jenna Orrow</div></div>
    <div class="member featured"><div class="member-photo tone-e" role="img" aria-label="Photo of a trainer doing push-ups"></div><div class="member-more">Learn More</div><div class="member-name">Priya Solen</div></div>
    <div class="member"><div class="member-photo tone-d" role="img" aria-label="Photo of a male trainer"></div><div class="member-name">Dario Kest</div></div>
    <div class="member"><div class="member-photo tone-c" role="img" aria-label="Photo of a volunteer stretching"></div><div class="member-name">Lena Farro</div></div>
    <div class="member"><div class="member-photo tone-b" role="img" aria-label="Photo of a volunteer with curly hair"></div><div class="member-name">Nadia Voss</div></div>
    <div class="member"><div class="member-photo tone-d" role="img" aria-label="Photo of a male volunteer"></div><div class="member-name">Omar Relis</div></div>
    <div class="member"><div class="member-photo tone-e" role="img" aria-label="Photo of a volunteer lifting weights"></div><div class="member-name">Tessa Brin</div></div>
    <div class="member"><div class="member-photo tone-a" role="img" aria-label="Photo of a volunteer training"></div><div class="member-name">Kira Dalm</div></div>
    <div class="member"><div class="member-photo tone-b" role="img" aria-label="Photo of a volunteer doing a plank"></div><div class="member-name">Sami Holt</div></div>
    <div class="member"><div class="member-photo tone-f" role="img" aria-label="Photo of a smiling trainer"></div><div class="member-name">Ava Meren</div></div>
    <div class="member"><div class="member-photo tone-c" role="img" aria-label="Photo of a trainer doing push-ups"></div><div class="member-name">Luca Penn</div></div>
  </div>
  <div class="more-row" style="top:1725px"><span class="btn">View more</span></div>

  <section class="about">
    <div class="about-text">
      <h2>About Us</h2>
      <p>Harbo Hale coordinates fitness trips to refugee camps around the globe, bringing certified trainers and volunteers together to share healthy habits, movement and joy.</p>
      <p>Lorem ipsum dolor sit amet, consectetur adipiscing elit, sed diam nonummy nibh euismod tincidunt ut laoreet dolore magna aliquam erat volutpat. Ut wisi enim ad minim veniam, quis nostrud exerci tation ullamcorper suscipit lobortis nisl ut aliquip ex ea commodo consequat. Duis autem vel eum iriure dolor in hendrerit in vulputate velit esse molestie consequat.</p>
      <p>Vel illum dolore eu feugiat nulla facilisis at vero eros et accumsan et iusto odio dignissim qui blandit praesent luptatum zzril delenit augue duis dolore te feugait nulla facilisi. Nam liber tempor cum soluta nobis eleifend option congue nihil imperdiet.</p>
      <div class="stats">
        <div class="stat"><b>+24</b><span>Countries</span></div>
        <div class="stat"><b>+57</b><span>Volunteers</span></div>
        <div class="stat"><b>+17</b><span>Summer camps</span></div>
      </div>
    </div>
    <div class="about-photo" role="img" aria-label="Photo of a group fitness class doing push-ups with dumbbells"></div>
  </section>

  <h2 class="section-title" style="top:2325px">Summer camps 2016</h2>
  <div class="camps">
    <article class="camp">
      <div class="camp-photo camp-1" role="img" aria-label="Photo of healthy lunch boxes and dumbbells"></div>
      <div class="camp-body"><div class="camp-meta"><span>12/06/2016</span><span>No comments</span></div><div class="camp-title">Healthy meals at the summer camp</div></div>
    </article>
    <article class="camp featured">
      <div class="camp-photo camp-2" role="img" aria-label="Photo of children playing at the beach"></div>
      <div class="camp-body"><div class="camp-meta"><span>18/06/2016</span><span>No comments</span></div><div class="camp-title">Fun and games on the beach</div></div>
    </article>
    <article class="camp">
      <div class="camp-photo camp-3" role="img" aria-label="Photo of children in a classroom at camp"></div>
      <div class="camp-body"><div class="camp-meta"><span>24/06/2016</span><span>No comments</span></div><div class="camp-title">Learning together at camp</div></div>
    </article>
  </div>
  <div class="more-row" style="top:2712px"><span class="btn">All news</span></div>

  <div class="partners" aria-label="Partner organisations">
    <span class="partner" style="width:150px;background:#5bb6e6"></span>
    <span class="partner" style="width:100px;border-radius:50%;background:#2c64b0"></span>
    <span class="partner" style="width:140px;background:#d8352f"></span>
    <span class="partner" style="width:200px;height:70px;border-radius:35px;background:#1d3f8f"></span>
    <span class="partner" style="width:100px;background:#1a9bd8"></span>
  </div>

  <footer class="footer">
    <div class="footer-cols">
      <div class="footer-col" style="width:360px">
        <h4>Harbo Hale</h4>
        <p>Harbo Hale is a non-profit based in San Francisco bringing fitness classes and healthy lifestyle support to refugee camps. Join a trip alone, as a group or with your corporate team.</p>
      </div>
      <div class="footer-col" style="width:220px">
        <h4>Contact us</h4>
        <p>100 Harbor Lane, Suite 4<br>San Francisco, CA 94100<br>+1 (555) 010-2040<br>hello@harbohale-example.org</p>
      </div>
      <div class="footer-col">
        <h4>Social networks</h4>
        <div class="social"><i style="background:var(--blue)"></i><i style="background:var(--green)"></i><i style="background:var(--blue-deep)"></i><i style="background:var(--green-dark)"></i></div>
      </div>
    </div>
    <div class="footer-bar">
      <span>© 2016 Harbo Hale</span>
      <ul><li class="active">Home</li><li>About us</li><li>Trips</li><li>Trainers/Hosts</li><li>Registration</li><li>Albums</li><li>Contact</li><li>Donate</li></ul>
      <span>+1 (555) 010-2040</span>
    </div>
  </footer>

</div>
</body>
</html>
```